Backup Software Tri-fold Brochure Project

We need a great looking and informative brochure to describe our new Backup Software offering. The brochures are to be used in retail and small business environments given to clients interested in protecting their computer from data loss.
The brochure should include attractive imagery that conveys a sense of Trust and Security to the prospective client.
The copy is provided as an attachment to this project. We'd like our Steady Deskframe product logo to be printed on the back cover. The logo is attached to this project.
The finished tri-fold brochure will be submitted to Quellpress for printing as an 8.5" x 11" tri-fold brochure. Their design instructions are online http://quellpress-example.com/custom-brochures.aspx.
The finished product should be Adobe Illustrator CS3 (*.ai) with a PDF Proof.
Target Market(s)
Retail and Small Business customers
Industry/Entity Type
Software
Colors
Designer to choose colors to be used in the design.
Look and feel

```html
<!DOCTYPE html>
<html lang="en">
<head>
<meta charset="utf-8">
<title>Steady Deskframe – Offsite Backup Tri-fold</title>
<link rel="stylesheet" href="https://fonts.googleapis.com/css2?family=Exo+2:wght@600;700;800&family=Open+Sans:wght@400;600;700&display=swap">
<style>
  :root {
    --bg: #2b2b2b;
    --paper: #ffffff;
    --paper-shade: #eeeff0;
    --blue: #1d6fb8;
    --blue-deep: #15589a;
    --green: #55b63a;
    --ink: #333333;
    --link: #1d5fa8;
    --photo-a: #c9d3da;
    --photo-b: #8c98a3;
  }
  * { box-sizing: border-box; margin: 0; padding: 0; }
  html, body { width: 1200px; height: 800px; overflow: hidden; background: var(--bg); }
  body { font-family: "Open Sans", Arial, sans-serif; color: var(--ink); }

  .brochure {
    position: absolute; left: 135px; top: 40px;
    width: 930px; height: 720px;
    display: flex;
  }
  .panel {
    position: relative; width: 310px; height: 720px;
    background: var(--paper); overflow: hidden;
  }
  .panel--middle { background: linear-gradient(90deg, var(--paper-shade), var(--paper) 30%, var(--paper)); }
  .panel--cover { background: linear-gradient(90deg, var(--paper-shade), var(--paper) 25%); }

  .band { position: absolute; left: 0; bottom: 0; width: 310px; }

  .display { font-family: "Exo 2", Arial, sans-serif; font-weight: 800; text-transform: uppercase; letter-spacing: .5px; }

  /* inside panel */
  .story { position: relative; z-index: 1; padding: 48px 30px 0 30px; }
  .story__title { color: var(--blue); font-size: 19px; line-height: 1.15; margin-bottom: 18px; }
  .story__body p { font-size: 10.5px; line-height: 1.42; text-align: justify; margin-bottom: 11px; }
  .tagline {
    position: absolute; left: 30px; bottom: 26px; color: #fff;
    font-family: "Exo 2", Arial, sans-serif; font-weight: 700; font-size: 26px; line-height: 1.1;
  }
  .tagline strong { font-weight: 800; text-transform: uppercase; display: block; }

  /* facts panel */
  .facts { padding: 54px 22px 0; text-align: center; }
  .facts__title { color: var(--blue); font-size: 22px; margin-bottom: 16px; }
  .facts__sub { font-family: "Open Sans", sans-serif; font-weight: 700; font-size: 14px; margin-bottom: 8px; }
  .facts__list { list-style: none; font-size: 10.5px; line-height: 1.6; }
  .facts__list li::before { content: "* "; }

  .brand { display: flex; align-items: center; justify-content: center; gap: 8px; }
  .brand__mark { width: 16px; height: 16px; background: var(--green); }
  .brand__name { font-family: "Exo 2", Arial, sans-serif; font-weight: 800; text-transform: uppercase; color: var(--blue); }
  .facts .brand { margin: 26px 0 22px; }
  .facts .brand__name { font-size: 19px; }

  .schedule { font-size: 14px; line-height: 1.25; color: #222; }
  .phone { font-family: "Exo 2", Arial, sans-serif; font-weight: 800; font-size: 30px; color: #111; margin: 6px 0 20px; }
  .sources { list-style: none; font-size: 9.5px; line-height: 1.35; color: var(--link); }
  .sources li { margin-bottom: 6px; word-break: break-all; }
  .legal { font-size: 8px; margin-top: 12px; line-height: 1.4; }
  .web {
    position: absolute; left: 0; right: 0; bottom: 34px; text-align: center;
    color: #fff; font-size: 17px; letter-spacing: 1px;
  }

  /* cover panel */
  .cover { padding: 56px 20px 0; text-align: center; }
  .cover .brand__name { font-size: 22px; }
  .headline { margin-top: 40px; font-size: 27px; line-height: 1.1; }
  .headline .blue { color: var(--blue); }
  .headline .green { color: var(--green); }
  .photo {
    position: absolute; left: 0; top: 300px; width: 310px; height: 250px;
    background: linear-gradient(160deg, var(--photo-a), var(--photo-b));
  }
  .cover-call {
    position: absolute; left: 0; right: 0; bottom: 40px; text-align: center; color: #fff;
    font-family: "Exo 2", Arial, sans-serif; font-weight: 800; text-transform: uppercase;
  }
  .cover-call span { display: block; font-size: 22px; }
  .cover-call b { display: block; font-size: 30px; }
</style>
</head>
<body>
<main class="brochure">

  <section class="panel panel--inside">
    <div class="story">
      <h2 class="story__title display">Your Entire Digital Life<br>Is At Risk</h2>
      <div class="story__body">
        <p>Your computer stores everything you've ever created. Everything you've written, every email you've sent, every list you've made, every picture you've taken or movie you've made, all music you've created, your proposals, your spreadsheets, your presentations, your word files, your artwork, programs you've written, anything you've dictated, and much more... All your digital life is stored on your computer and is at risk of loss without backup.</p>
        <p>And your computer stores a copy of all your personal information. Your passwords, your online banking, your PINs, your credit cards and all your health and shopping records. This makes it a juicy target for hackers. Every day your digital life is exposed to computer viruses, Malware and spammers all trying to break in. If they succeed the damage could be incalculable.</p>
        <p>If hackers destroy your information or a simple hard drive failure happens, restoring your programs will cost you days of effort and potentially hundreds of dollars. But your files could be unrecoverable. This means the loss of everything you've ever created.</p>
      </div>
    </div>
    <svg class="band" width="310" height="185" viewBox="0 0 310 185" aria-hidden="true">
      <path d="M0 58 Q150 18 310 8 L310 185 L0 185 Z" fill="var(--blue)"/>
      <path d="M0 50 Q150 10 310 0" fill="none" stroke="var(--green)" stroke-width="4"/>
    </svg>
    <p class="tagline">The Only<br>Protection is a<strong>Great Backup.</strong></p>
  </section>

  <section class="panel panel--middle">
    <div class="facts">
      <h2 class="facts__title display">Did You Know?</h2>
      <p class="facts__sub">Every Week (in the US)</p>
      <ul class="facts__list">
        <li>140,000 drives crash</li>
        <li>12,000 laptops are lost or stolen</li>
        <li>37,000 Internet Crimes are committed</li>
        <li>Internet criminals steal $25 Million</li>
      </ul>
      <div class="brand"><span class="brand__mark"></span><span class="brand__name">Steady Deskframe</span></div>
      <p class="schedule display">Call us to schedule<br>a day to bring in<br>your computer.</p>
      <p class="phone">0123 456 789</p>
      <ul class="sources">
        <li>http://www.laptopwatch-example.com/reports/lost_laptop_study.pdf</li>
        <li>http://research.drivecount-example.org/archive/disk_failures.pdf</li>
        <li>https://www.netcrimedesk-example.gov/annualreport/2016_Report.pdf</li>
      </ul>
      <p class="legal">Copyright(c) 2017, Brannock Systems, Inc.<br>All Rights Reserved</p>
    </div>
    <svg class="band" width="310" height="130" viewBox="0 0 310 130" aria-hidden="true">
      <path d="M0 40 Q160 30 310 0 L310 130 L0 130 Z" fill="var(--blue)"/>
      <path d="M0 32 Q160 22 310 -8" fill="none" stroke="var(--green)" stroke-width="4"/>
    </svg>
    <p class="web">www.yourweb.com</p>
  </section>

  <section class="panel panel--cover">
    <div class="cover">
      <div class="brand"><span class="brand__mark"></span><span class="brand__name">Steady Deskframe</span></div>
      <h1 class="headline display">
        <span class="blue">Your Entire</span><br>
        <span class="green">Digital Life is</span><br>
        <span class="blue">At Risk!</span>
      </h1>
    </div>
    <div class="photo" role="img" aria-label="Photo of a frustrated businessman in a suit throwing up his hands at a laptop in a bright office"></div>
    <svg class="band" width="310" height="220" viewBox="0 0 310 220" aria-hidden="true">
      <path d="M0 60 Q170 50 310 0 L310 220 L0 220 Z" fill="var(--blue)"/>
      <path d="M0 50 Q170 40 310 -10" fill="none" stroke="var(--green)" stroke-width="10"/>
    </svg>
    <p class="cover-call"><span>Call Now</span><b>0123 456 789</b></p>
  </section>

</main>
</body>
</html>
```